Website Re-design

Hi, I'm looking for help in redesigning my web site. I currently have a site www.brightmoorlamps.example where I sell lamps, and while I like some aspects of the design, you can tell that I have done the graphics myself and am not a pro at it. I'd like help in redesigning it, and am open to completely new design graphics. I have made the 3 slider images myself, and I feel they could be a bit better, but I am not sure how to do it. For example, on the homepage, the 'About Us', 'Secured Shopping', and '$10 Off' graphics don't go well with the rest of the page. I would like more cohesion in the design and more visual interest in the header, which is pretty basic right now. Also, that the bottom footer is black, I would like instead something else. I am looking for just the layout of the homepage, and possibly once that is done to work on more visual interest in some of the informational pages and product pages. I am looking for just the design in the form of a photoshop file or files that I can incorporate into my site. Thank you!
Updates

Project Deadline Extended
Reason: I just made this project payment committed, so I'd like a chance for designers who only choose payment committed projects to submit artwork. Thank you.

This project is now payment guaranteed/ committed.  Thanks.

Industry/Entity Type

Shopping

```html
<!DOCTYPE html>
<html lang="en">
<head>
<meta charset="utf-8">
<title>Brightmoor Lamps – Home</title>
<link href="https://fonts.googleapis.com/css2?family=Varela+Round&family=Caveat:wght@500&display=swap" rel="stylesheet">
<style>
  :root{
    --page-bg:#b9b9b9;
    --panel-bg:#e3e3e3;
    --footer-bg:#e1e1e1;
    --rule:#3a2a35;
    --ink:#4a4a4a;
    --ink-soft:#7b7b7b;
    --white:#ffffff;
    --blush:#e8a9a9;
    --dot-pink:#e3b1b1;
    --dot-blue:#9cc5cc;
    --card-head:#cfe3e8;
    --card-body:rgba(222,222,222,.72);
    --caption:#3a2030;
    --social:#a9cdd2;
  }
  *{box-sizing:border-box;margin:0;padding:0}
  html,body{width:1200px;height:1200px;overflow:hidden}
  body{position:relative;background:var(--page-bg);font-family:"Varela Round",Arial,sans-serif;color:var(--ink)}
  .abs{position:absolute}

  .brand{left:74px;top:40px;display:flex;align-items:center;gap:12px}
  .brand-mark{width:30px;height:30px;border-radius:50%;background:var(--ink)}
  .brand-name{font-size:30px;line-height:1;color:var(--ink);letter-spacing:1px}

  .main-nav{top:90px;left:0;font-size:17px;letter-spacing:2px}
  .main-nav a{position:absolute;white-space:nowrap;color:#2f2f2f;text-decoration:none}
  .main-nav a.is-current{color:var(--white)}

  .header-rule{left:67px;top:128px;width:1037px;height:3px;background:var(--rule)}

  .hero{left:67px;top:131px;width:1037px;height:552px;background:var(--panel-bg);overflow:hidden}
  .hero-glow{left:60px;top:100px;width:600px;height:300px;border-radius:50%;
    background:radial-gradient(ellipse at center,var(--blush) 0%,rgba(232,169,169,.75) 45%,rgba(232,169,169,0) 72%)}
  .hero-title{left:176px;top:170px;font-size:40px;color:var(--white);letter-spacing:3px;font-weight:400}
  .hero-product{left:701px;top:22px;width:218px;height:525px;
    background:linear-gradient(180deg,#fbfbfb 0%,#e9e9e9 36%,#a0789c 45%,#8a5a86 75%,#d9d4d9 100%);
    border-radius:8px 8px 4px 4px}
  .hero-caption{left:200px;top:476px;font-family:"Caveat",cursive;font-size:38px;color:var(--caption);letter-spacing:3px;white-space:nowrap}

  .texture-band{left:0;top:686px;width:1200px;height:360px;
    background:linear-gradient(160deg,#9aa0a4 0%,#7f868b 35%,#959ca0 60%,#767d82 100%)}

  .slider-dots{left:0;top:723px}
  .slider-dots span{position:absolute;width:22px;height:22px;border-radius:50%}
  .dot-white{left:516px;background:var(--white)}
  .dot-pink{left:574px;background:var(--dot-pink)}
  .dot-blue{left:640px;background:var(--dot-blue)}

  .promo{background:var(--card-body)}
  .promo-head{height:38px;background:var(--card-head);color:var(--white);font-size:22px;letter-spacing:2px;line-height:38px;text-align:center}
  .promo-text{font-size:11px;line-height:17px;letter-spacing:.6px;color:#333;padding:14px 60px 0 8px}
  .promo-about{left:102px;top:848px;width:254px;height:124px}
  .promo-secure{left:438px;top:845px;width:308px;height:124px}
  .promo-secure .promo-text{padding-left:56px;padding-right:50px}
  .promo-offer{left:826px;top:845px;width:259px;height:124px}
  .promo-offer .promo-text{padding:20px 24px 0 50px;line-height:19px}

  .site-footer{left:67px;top:1047px;width:1037px;height:153px;background:var(--footer-bg)}
  .footer-col{top:38px;width:120px}
  .footer-col h4{font-size:10px;font-weight:400;letter-spacing:1.2px;color:var(--ink-soft);margin-bottom:12px}
  .footer-col li{list-style:none;font-size:8.5px;line-height:11.6px;letter-spacing:.6px;color:var(--ink-soft)}
  .col-help{left:67px}.col-account{left:190px}.col-about{left:311px}.col-contact{left:434px;width:180px}

  .social{left:0;top:0}
  .social span{position:absolute;top:14px;width:40px;height:40px;border-radius:50%;background:var(--social)}
  .social .s1{left:810px}.social .s2{left:865px}.social .s3{left:920px}

  .newsletter{left:709px;top:85px;width:307px;height:38px;background:#f2f2f2;
    box-shadow:inset 0 3px 4px rgba(0,0,0,.25);font-size:11px;letter-spacing:.5px;color:#333;line-height:38px;padding-left:8px}
</style>
</head>
<body>
  <header>
    <div class="brand abs"><span class="brand-mark"></span><span class="brand-name">brightmoor lamps</span></div>
    <nav class="main-nav abs">
      <a class="is-current" href="#" style="left:357px">HOME</a>
      <a href="#" style="left:474px">SHOP</a>
      <a href="#" style="left:590px">ABOUT US</a>
      <a href="#" style="left:743px">CONTACT US</a>
    </nav>
    <div class="header-rule abs"></div>
  </header>

  <section class="hero abs">
    <div class="hero-glow abs"></div>
    <h1 class="hero-title abs">a touch of glass</h1>
    <div class="hero-product abs" role="img" aria-label="Photo of a cut-glass violet table lamp with a white drum shade"></div>
    <p class="hero-caption abs">“the Violet Lattice” Table Lamp</p>
  </section>

  <section class="texture-band abs" role="img" aria-label="Photo of grey weathered tree bark texture"></section>

  <div class="slider-dots abs"><span class="dot-white"></span><span class="dot-pink"></span><span class="dot-blue"></span></div>

  <article class="promo promo-about abs">
    <div class="promo-head">about us &nbsp;&gt;&gt;</div>
    <p class="promo-text">Brightmoor Lamps provides beautiful and artistic home and hospitality lighting.</p>
  </article>
  <article class="promo promo-secure abs">
    <div class="promo-head">secured shopping &nbsp;&gt;&gt;</div>
    <p class="promo-text">Brightmoor Lamps provides beautiful and artistic home and hospitality lighting.</p>
  </article>
  <article class="promo promo-offer abs">
    <div class="promo-head">$10 off &gt;&gt;</div>
    <p class="promo-text">Brightmoor Lamps provides beautiful and artistic home and hospitality lighting.</p>
  </article>

  <footer class="site-footer abs">
    <div class="footer-col col-help abs"><h4>HELP + INFO</h4><ul><li>Contact Us</li><li>Shipping Info</li><li>Returns</li><li>To the Trade</li><li>Privacy Policy</li><li>Terms of use</li></ul></div>
    <div class="footer-col col-account abs"><h4>MY ACCOUNT</h4><ul><li>Sign In</li><li>Order Status</li><li>Order History</li><li>View Cart</li><li>Checkout</li></ul></div>
    <div class="footer-col col-about abs"><h4>ABOUT US</h4><ul><li>Who We Are</li><li>Testimonials</li></ul></div>
    <div class="footer-col col-contact abs"><h4>CONTACT</h4><ul><li>Contact Us</li><li>info@brightmoorlamps.example</li></ul></div>
    <div class="social abs"><span class="s1"></span><span class="s2"></span><span class="s3"></span></div>
    <div class="newsletter abs">Enter E-mail for news, &nbsp;sales and exclusive offers.</div>
  </footer>
</body>
</html>
```